A2 Desk calendar/planner *landscape*

We need a promotional a2 desk calendar for our customers (examples attached). Basically a marketing item so that our business is always fresh in the customer's mind sitting at their desk. It needs to be a2 Landscape as it will be a 20-page tear-off pad. Including logos, possibly images, 2020/21 calendar years, a big section in middle for writing on like examples. Business details and possibly a list of our industries and products. I have lots of images, logos and any other information visit www.brompellink.com.au to get an idea of what we do.
Industry/Entity Type
Hydraulic
Colors
Designer to choose colors to be used in the design.
Requirements
Must have
- Buisness logo, 2020 and 2021 calander year boxes like examples attached, colour themebluje and white possiby to go with the our logo. website adress phone number info. australian holiday dates . slogan "Your trusted partner for hose and fittings"
Nice to have
- public holiday dates from ; https://www.tollimark.com.au/law-compliance/laws-regulations/public-holidays

```html
<!DOCTYPE html>
<html lang="en">
<head>
<meta charset="utf-8">
<title>Brompel Hose and Fittings – 2020/21 Desk Planner</title>
<link rel="stylesheet" href="https://fonts.googleapis.com/css2?family=Montserrat:ital,wght@0,600;0,700;0,800;1,800&family=Open+Sans:ital,wght@0,400;0,600;0,700;1,700&display=swap">
<style>
:root{
  --brand-blue:#1731c2;
  --title-blue:#1838c9;
  --ink:#1c1c1c;
  --white:#ffffff;
  --week-green:#2e9b3a;
  --holiday-red:#e0141b;
  --dot-grey:#d4d4d4;
  --faint-grey:#c9c9c9;
  --rule-grey:#cfcfcf;
}
*{margin:0;padding:0;box-sizing:border-box}
html,body{width:1200px;height:849px;overflow:hidden}
body{position:relative;background:var(--brand-blue);font-family:"Open Sans",Arial,sans-serif;color:var(--ink)}

/* header */
.masthead{position:absolute;left:0;top:0;width:1200px;height:116px;background:var(--white)}
.brand{position:absolute;left:25px;top:20px;display:flex;align-items:center;gap:10px}
.brand-dot{width:62px;height:62px;border-radius:50%;background:var(--ink)}
.brand-name{font-family:"Montserrat",sans-serif;font-weight:800;color:var(--brand-blue);line-height:1}
.brand-name .big{display:block;font-size:33px;letter-spacing:2px}
.brand-name .small{display:block;font-size:12.5px;letter-spacing:3.2px;margin-top:4px}
.tagline{position:absolute;left:86px;top:82px;font-size:13px;font-weight:700;font-style:italic;color:var(--ink)}
.photo{position:absolute;top:18px;width:107px;height:86px;border:1px solid var(--brand-blue);border-radius:3px}
.photo.p1{left:406px;background:linear-gradient(135deg,#8fa6c0,#c9d2dc 50%,#7d8590)}
.photo.p2{left:534px;background:linear-gradient(160deg,#f4f4f4,#3a3a3a 40%,#55d33a 60%,#f4f4f4)}
.photo.p3{left:663px;background:linear-gradient(150deg,#f5f5f5,#2b2b2b 45%,#b5b5b5 70%,#f5f5f5)}
.photo.p4{left:796px;background:linear-gradient(135deg,#f2f2f2,#8c8c8c 50%,#e8e8e8)}
.photo.p5{left:923px;background:linear-gradient(135deg,#9aa3ad,#1e1e1e 45%,#c8262b 60%,#5a5a5a)}
.contact{position:absolute;left:1040px;top:24px;font-size:8.4px;line-height:12.8px;white-space:nowrap}
.contact h2{font-family:"Montserrat",sans-serif;font-variant:small-caps;font-size:10.5px;letter-spacing:1.5px;color:var(--title-blue);font-weight:700;line-height:11px;margin-bottom:3px}
.contact strong{font-weight:600}

/* panels */
.panel{position:absolute;background:var(--white);border-radius:4px}
.smallcaps{font-family:"Montserrat",sans-serif;font-variant:small-caps;letter-spacing:1.2px}

.products{left:26px;top:130px;width:204px;height:261px;padding:13px 0 0 12px}
.products h3{font-size:10px;font-weight:700;color:var(--title-blue);line-height:13px}
.products ul{list-style:none}
.products li{font-size:8.2px;line-height:12.8px;font-weight:600;white-space:nowrap}
.products li.main::before{content:"•";margin-right:3px}
.products li.main{padding-left:3px;font-size:8.8px;font-weight:700}
.products li.sub{padding-left:23px;font-weight:600}
.products li.wrap{white-space:normal;padding-left:13px;text-indent:-10px;width:190px}
.products .services{margin-top:9px}
.products .services + ul li.main{font-weight:600;font-size:8.2px}

.todo{left:26px;top:412px;width:204px;height:409px}
.todo h3{position:absolute;left:12px;top:16px;font-size:10px;font-weight:700;line-height:13px}
.todo .lines{position:absolute;left:5px;right:5px;top:38px;height:372px;
  background:repeating-linear-gradient(to bottom,transparent 0 19.2px,var(--rule-grey) 19.2px 20px)}

.notes{left:253px;top:130px;width:592px;height:539px;
  background-color:#fbfbfb;
  background-image:radial-gradient(circle,var(--dot-grey) 0.9px,transparent 1.2px);
  background-size:5px 5px;
  display:flex;align-items:center;justify-content:center}
.notes .faint-name{font-family:"Montserrat",sans-serif;font-weight:800;font-size:30px;letter-spacing:3px;color:var(--faint-grey)}

.holidays{left:253px;top:690px;width:592px;height:131px}
.holidays h3{position:absolute;left:18px;top:8px;font-size:10px;font-weight:700;line-height:13px}
.holiday-year{position:absolute;top:22px}
.holiday-year h4{font-size:10px;font-weight:700;color:var(--title-blue);line-height:13px}
.holiday-year.y2020{left:18px}
.holiday-year.y2021{left:304px}
.holiday-cols{display:flex;padding-left:8px}
.holiday-cols ul{list-style:none;font-size:8.4px;line-height:12.8px;letter-spacing:.2px;white-space:nowrap}
.holiday-cols ul:first-child{width:134px}

/* calendars */
.calendars{left:870px;top:130px;width:309px;height:691px}
.year-title{position:absolute;left:0;width:100%;text-align:center;font-size:11px;font-weight:700;color:var(--title-blue)}
.year-title.t2020{top:12px}
.year-title.t2021{top:353px}
.year{position:absolute;left:14px;display:grid;grid-template-columns:repeat(3,86px);column-gap:10px}
.year.y2020{top:34px;grid-auto-rows:82px}
.year.y2021{top:375px;grid-template-rows:83px 81px 74px 76px}
.month h4{font-size:5.4px;font-weight:700;text-align:center;line-height:9px}
.days{display:grid;grid-template-columns:repeat(8,1fr);grid-auto-rows:9.1px;font-size:5px;line-height:9.1px;text-align:center}
.days .dh{font-weight:700}
.days b{font-weight:400;color:var(--week-green);font-size:4.4px}
.days .hol{color:var(--holiday-red);font-weight:700}
.from-sun{grid-column:2}.from-mon{grid-column:3}.from-tue{grid-column:4}.from-wed{grid-column:5}
.from-thu{grid-column:6}.from-fri{grid-column:7}.from-sat{grid-column:8}
</style>
</head>
<body>

<header class="masthead">
  <div class="brand">
    <div class="brand-dot"></div>
    <div class="brand-name"><span class="big">BROMPEL</span><span class="small">HOSE AND FITTINGS</span></div>
  </div>
  <p class="tagline">"Your trusted partner for hose and fittings"</p>
  <div class="photo p1" role="img" aria-label="Photo of hydraulic machinery with braided hose lines"></div>
  <div class="photo p2" role="img" aria-label="Photo of industrial hoses with couplings"></div>
  <div class="photo p3" role="img" aria-label="Photo of hydraulic hoses with crimped fittings"></div>
  <div class="photo p4" role="img" aria-label="Photo of hydraulic valves, fittings and adaptors"></div>
  <div class="photo p5" role="img" aria-label="Photo of a hose crimping machine"></div>
  <div class="contact">
    <h2>Contact Us</h2>
    <p><strong>Website:</strong> brompellink.com.au/</p>
    <p><strong>Phone (24/7):</strong> 0400 555 123</p>
    <p><strong>Sales and service:</strong> 0400 555 123</p>
    <p><strong>General enquiries:</strong> 08 8000 4411</p>
    <p><strong>Email:</strong> info@brompellink.com.au</p>
  </div>
</header>

<section class="panel products smallcaps">
  <h3>Our Products</h3>
  <ul>
    <li class="main">Hose</li>
    <li class="sub">Hydraulic Hose</li>
    <li class="sub">Industrial Hose</li>
    <li class="sub">Thermoplastic Hose</li>
    <li class="sub">PFTE Hose</li>
    <li class="main">Fittings</li>
    <li class="sub">Hose Tails</li>
    <li class="sub">Couplings</li>
    <li class="sub">Adaptors</li>
    <li class="main wrap">House Assembly Manufacturing Unit</li>
    <li class="main">Hydraulic Componentry</li>
  </ul>
  <h3 class="services">Our Services</h3>
  <ul>
    <li class="main">Onsite Services</li>
    <li class="main">Onsite Mobile Workshops</li>
    <li class="main">Distributor/ Workshop Fit-Out</li>
  </ul>
</section>

<section class="panel todo">
  <h3 class="smallcaps">To Do list</h3>
  <div class="lines"></div>
</section>

<section class="panel notes">
  <span class="faint-name">BROMPEL</span>
</section>

<section class="panel holidays">
  <h3 class="smallcaps">Holidays</h3>
  <div class="holiday-year y2020">
    <h4>Year 2020</h4>
    <div class="holiday-cols">
      <ul>
        <li>01 JAN - New Year's Day</li><li>27 JAN - Australia Day</li><li>09 MAR - Canberra Day</li>
        <li>10 APR - Good Friday</li><li>11 APR - Easter Saturday</li><li>12 APR - Easter Sunday</li><li>13 APR - Easter Monday</li>
      </ul>
      <ul>
        <li>25 APR - Anzac Day</li><li>01 JUN - Reconciliation Day</li><li>08 JUN - Queen's Birthday</li>
        <li>05 OCT - Labour Day</li><li>25 DEC - Christmas Day</li><li>28 DEC - Boxing Day</li>
      </ul>
    </div>
  </div>
  <div class="holiday-year y2021">
    <h4>Year 2021</h4>
    <div class="holiday-cols">
      <ul>
        <li>01 JAN - New Year's Day</li><li>26 JAN - Australia Day</li><li>08 MAR - Canberra Day</li>
        <li>02 APR - Good Friday</li><li>03 APR - Easter Saturday</li><li>04 APR - Easter Sunday</li><li>05 APR - Easter Monday</li>
      </ul>
      <ul>
        <li>25 APR - Anzac Day</li><li>31 MAY - Reconciliation Day</li><li>14 JUN - Queen's Birthday</li>
        <li>04 OCT - Labour Day</li><li>25 DEC - Christmas Day</li><li>26 DEC - Boxing Day</li>
      </ul>
    </div>
  </div>
</section>

<section class="panel calendars">
  <h2 class="year-title t2020">2020 Calendar</h2>
  <div class="year y2020">
    <div class="month"><h4>January 2020</h4><div class="days">
      <span class="dh">W</span><span class="dh">S</span><span class="dh">M</span><span class="dh">T</span><span class="dh">W</span><span class="dh">T</span><span class="dh">F</span><span class="dh">S</span>
      <b>1</b><span class="from-wed hol">1</span><span>2</span><span>3</span><span>4</span>
      <b>2</b><span>5</span><span>6</span><span>7</span><span>8</span><span>9</span><span>10</span><span>11</span>
      <b>3</b><span>12</span><span>13</span><span>14</span><span>15</span><span>16</span><span>17</span><span>18</span>
      <b>4</b><span>19</span><span>20</span><span>21</span><span>22</span><span>23</span><span>24</span><span>25</span>
      <b>5</b><span>26</span><span class="hol">27</span><span>28</span><span>29</span><span>30</span><span>31</span>
    </div></div>
    <div class="month"><h4>February 2020</h4><div class="days">
      <span class="dh">W</span><span class="dh">S</span><span class="dh">M</span><span class="dh">T</span><span class="dh">W</span><span class="dh">T</span><span class="dh">F</span><span class="dh">S</span>
      <b>5</b><span class="from-sat">1</span>
      <b>6</b><span>2</span><span>3</span><span>4</span><span>5</span><span>6</span><span>7</span><span>8</span>
      <b>7</b><span>9</span><span>10</span><span>11</span><span>12</span><span>13</span><span>14</span><span>15</span>
      <b>8</b><span>16</span><span>17</span><span>18</span><span>19</span><span>20</span><span>21</span><span>22</span>
      <b>9</b><span>23</span><span>24</span><span>25</span><span>26</span><span>27</span><span>28</span><span>29</span>
    </div></div>
    <div class="month"><h4>March 2020</h4><div class="days">
      <span class="dh">W</span><span class="dh">S</span><span class="dh">M</span><span class="dh">T</span><span class="dh">W</span><span class="dh">T</span><span class="dh">F</span><span class="dh">S</span>
      <b>10</b><span class="from-sun">1</span><span>2</span><span>3</span><span>4</span><span>5</span><span>6</span><span>7</span>
      <b>11</b><span>8</span><span class="hol">9</span><span>10</span><span>11</span><span>12</span><span>13</span><span>14</span>
      <b>12</b><span>15</span><span>16</span><span>17</span><span>18</span><span>19</span><span>20</span><span>21</span>
      <b>13</b><span>22</span><span>23</span><span>24</span><span>25</span><span>26</span><span>27</span><span>28</span>
      <b>14</b><span>29</span><span>30</span><span>31</span>
    </div></div>
    <div class="month"><h4>April 2020</h4><div class="days">
      <span class="dh">W</span><span class="dh">S</span><span class="dh">M</span><span class="dh">T</span><span class="dh">W</span><span class="dh">T</span><span class="dh">F</span><span class="dh">S</span>
      <b>14</b><span class="from-wed">1</span><span>2</span><span>3</span><span>4</span>
      <b>15</b><span>5</span><span>6</span><span>7</span><span>8</span><span>9</span><span class="hol">10</span><span class="hol">11</span>
      <b>16</b><span class="hol">12</span><span class="hol">13</span><span>14</span><span>15</span><span>16</span><span>17</span><span>18</span>
      <b>17</b><span>19</span><span>20</span><span>21</span><span>22</span><span>23</span><span>24</span><span class="hol">25</span>
      <b>18</b><span>26</span><span>27</span><span>28</span><span>29</span><span>30</span>
    </div></div>
    <div class="month"><h4>May 2020</h4><div class="days">
      <span class="dh">W</span><span class="dh">S</span><span class="dh">M</span><span class="dh">T</span><span class="dh">W</span><span class="dh">T</span><span class="dh">F</span><span class="dh">S</span>
      <b>18</b><span class="from-fri">1</span><span>2</span>
      <b>19</b><span>3</span><span>4</span><span>5</span><span>6</span><span>7</span><span>8</span><span>9</span>
      <b>20</b><span>10</span><span>11</span><span>12</span><span>13</span><span>14</span><span>15</span><span>16</span>
      <b>21</b><span>17</span><span>18</span><span>19</span><span>20</span><span>21</span><span>22</span><span>23</span>
      <b>22</b><span>24</span><span>25</span><span>26</span><span>27</span><span>28</span><span>29</span><span>30</span>
      <b>23</b><span>31</span>
    </div></div>
    <div class="month"><h4>June 2020</h4><div class="days">
      <span class="dh">W</span><span class="dh">S</span><span class="dh">M</span><span class="dh">T</span><span class="dh">W</span><span class="dh">T</span><span class="dh">F</span><span class="dh">S</span>
      <b>23</b><span class="from-mon hol">1</span><span>2</span><span>3</span><span>4</span><span>5</span><span>6</span>
      <b>24</b><span>7</span><span class="hol">8</span><span>9</span><span>10</span><span>11</span><span>12</span><span>13</span>
      <b>25</b><span>14</span><span>15</span><span>16</span><span>17</span><span>18</span><span>19</span><span>20</span>
      <b>26</b><span>21</span><span>22</span><span>23</span><span>24</span><span>25</span><span>26</span><span>27</span>
      <b>27</b><span>28</span><span>29</span><span>30</span>
    </div></div>
    <div class="month"><h4>July 2020</h4><div class="days">
      <span class="dh">W</span><span class="dh">S</span><span class="dh">M</span><span class="dh">T</span><span class="dh">W</span><span class="dh">T</span><span class="dh">F</span><span class="dh">S</span>
      <b>27</b><span class="from-wed">1</span><span>2</span><span>3</span><span>4</span>
      <b>28</b><span>5</span><span>6</span><span>7</span><span>8</span><span>9</span><span>10</span><span>11</span>
      <b>29</b><span>12</span><span>13</span><span>14</span><span>15</span><span>16</span><span>17</span><span>18</span>
      <b>30</b><span>19</span><span>20</span><span>21</span><span>22</span><span>23</span><span>24</span><span>25</span>
      <b>31</b><span>26</span><span>27</span><span>28</span><span>29</span><span>30</span><span>31</span>
    </div></div>
    <div class="month"><h4>August 2020</h4><div class="days">
      <span class="dh">W</span><span class="dh">S</span><span class="dh">M</span><span class="dh">T</span><span class="dh">W</span><span class="dh">T</span><span class="dh">F</span><span class="dh">S</span>
      <b>31</b><span class="from-sat">1</span>
      <b>32</b><span>2</span><span class="hol">3</span><span>4</span><span>5</span><span>6</span><span>7</span><span>8</span>
      <b>33</b><span>9</span><span>10</span><span>11</span><span>12</span><span>13</span><span>14</span><span>15</span>
      <b>34</b><span>16</span><span>17</span><span>18</span><span>19</span><span>20</span><span>21</span><span>22</span>
      <b>35</b><span>23</span><span>24</span><span>25</span><span>26</span><span>27</span><span>28</span><span>29</span>
      <b>36</b><span>30</span><span>31</span>
    </div></div>
    <div class="month"><h4>September 2020</h4><div class="days">
      <span class="dh">W</span><span class="dh">S</span><span class="dh">M</span><span class="dh">T</span><span class="dh">W</span><span class="dh">T</span><span class="dh">F</span><span class="dh">S</span>
      <b>36</b><span class="from-tue">1</span><span>2</span><span>3</span><span>4</span><span>5</span>
      <b>37</b><span>6</span><span>7</span><span>8</span><span>9</span><span>10</span><span>11</span><span>12</span>
      <b>38</b><span>13</span><span>14</span><span>15</span><span>16</span><span>17</span><span>18</span><span>19</span>
      <b>39</b><span>20</span><span>21</span><span>22</span><span>23</span><span>24</span><span>25</span><span>26</span>
      <b>40</b><span>27</span><span>28</span><span>29</span><span>30</span>
    </div></div>
    <div class="month"><h4>October 2020</h4><div class="days">
      <span class="dh">W</span><span class="dh">S</span><span class="dh">M</span><span class="dh">T</span><span class="dh">W</span><span class="dh">T</span><span class="dh">F</span><span class="dh">S</span>
      <b>40</b><span class="from-thu">1</span><span>2</span><span>3</span>
      <b>41</b><span>4</span><span class="hol">5</span><span>6</span><span>7</span><span>8</span><span>9</span><span>10</span>
      <b>42</b><span>11</span><span>12</span><span>13</span><span>14</span><span>15</span><span>16</span><span>17</span>
      <b>43</b><span>18</span><span>19</span><span>20</span><span>21</span><span>22</span><span>23</span><span>24</span>
      <b>44</b><span>25</span><span>26</span><span>27</span><span>28</span><span>29</span><span>30</span><span>31</span>
    </div></div>
    <div class="month"><h4>November 2020</h4><div class="days">
      <span class="dh">W</span><span class="dh">S</span><span class="dh">M</span><span class="dh">T</span><span class="dh">W</span><span class="dh">T</span><span class="dh">F</span><span class="dh">S</span>
      <b>45</b><span class="from-sun">1</span><span>2</span><span>3</span><span>4</span><span>5</span><span>6</span><span>7</span>
      <b>46</b><span>8</span><span>9</span><span>10</span><span>11</span><span>12</span><span>13</span><span>14</span>
      <b>47</b><span>15</span><span>16</span><span>17</span><span>18</span><span>19</span><span>20</span><span>21</span>
      <b>48</b><span>22</span><span>23</span><span>24</span><span>25</span><span>26</span><span>27</span><span>28</span>
      <b>49</b><span>29</span><span>30</span>
    </div></div>
    <div class="month"><h4>December 2020</h4><div class="days">
      <span class="dh">W</span><span class="dh">S</span><span class="dh">M</span><span class="dh">T</span><span class="dh">W</span><span class="dh">T</span><span class="dh">F</span><span class="dh">S</span>
      <b>49</b><span class="from-tue">1</span><span>2</span><span>3</span><span>4</span><span>5</span>
      <b>50</b><span>6</span><span>7</span><span>8</span><span>9</span><span>10</span><span>11</span><span>12</span>
      <b>51</b><span>13</span><span>14</span><span>15</span><span>16</span><span>17</span><span>18</span><span>19</span>
      <b>52</b><span>20</span><span>21</span><span>22</span><span>23</span><span>24</span><span class="hol">25</span><span class="hol">26</span>
      <b>53</b><span class="hol">27</span><span class="hol">28</span><span>29</span><span>30</span><span>31</span>
    </div></div>
  </div>

  <h2 class="year-title t2021">2021 Calendar</h2>
  <div class="year y2021">
    <div class="month"><h4>January 2021</h4><div class="days">
      <span class="dh">W</span><span class="dh">S</span><span class="dh">M</span><span class="dh">T</span><span class="dh">W</span><span class="dh">T</span><span class="dh">F</span><span class="dh">S</span>
      <b>53</b><span class="from-fri hol">1</span><span>2</span>
      <b>1</b><span>3</span><span>4</span><span>5</span><span>6</span><span>7</span><span>8</span><span>9</span>
      <b>2</b><span>10</span><span>11</span><span>12</span><span>13</span><span>14</span><span>15</span><span>16</span>
      <b>3</b><span>17</span><span>18</span><span>19</span><span>20</span><span>21</span><span>22</span><span>23</span>
      <b>4</b><span>24</span><span>25</span><span class="hol">26</span><span>27</span><span>28</span><span>29</span><span>30</span>
      <b>5</b><span>31</span>
    </div></div>
    <div class="month"><h4>February 2021</h4><div class="days">
      <span class="dh">W</span><span class="dh">S</span><span class="dh">M</span><span class="dh">T</span><span class="dh">W</span><span class="dh">T</span><span class="dh">F</span><span class="dh">S</span>
      <b>5</b><span class="from-mon">1</span><span>2</span><span>3</span><span>4</span><span>5</span><span>6</span>
      <b>6</b><span>7</span><span>8</span><span>9</span><span>10</span><span>11</span><span>12</span><span>13</span>
      <b>7</b><span>14</span><span>15</span><span>16</span><span>17</span><span>18</span><span>19</span><span>20</span>
      <b>8</b><span>21</span><span>22</span><span>23</span><span>24</span><span>25</span><span>26</span><span>27</span>
      <b>9</b><span>28</span>
    </div></div>
    <div class="month"><h4>March 2021</h4><div class="days">
      <span class="dh">W</span><span class="dh">S</span><span class="dh">M</span><span class="dh">T</span><span class="dh">W</span><span class="dh">T</span><span class="dh">F</span><span class="dh">S</span>
      <b>9</b><span class="from-mon">1</span><span>2</span><span>3</span><span>4</span><span>5</span><span>6</span>
      <b>10</b><span>7</span><span class="hol">8</span><span>9</span><span>10</span><span>11</span><span>12</span><span>13</span>
      <b>11</b><span>14</span><span>15</span><span>16</span><span>17</span><span>18</span><span>19</span><span>20</span>
      <b>12</b><span>21</span><span>22</span><span>23</span><span>24</span><span>25</span><span>26</span><span>27</span>
      <b>13</b><span>28</span><span>29</span><span>30</span><span>31</span>
    </div></div>
    <div class="month"><h4>April 2021</h4><div class="days">
      <span class="dh">W</span><span class="dh">S</span><span class="dh">M</span><span class="dh">T</span><span class="dh">W</span><span class="dh">T</span><span class="dh">F</span><span class="dh">S</span>
      <b>13</b><span class="from-thu">1</span><span class="hol">2</span><span class="hol">3</span>
      <b>14</b><span class="hol">4</span><span class="hol">5</span><span>6</span><span>7</span><span>8</span><span>9</span><span>10</span>
      <b>15</b><span>11</span><span>12</span><span>13</span><span>14</span><span>15</span><span>16</span><span>17</span>
      <b>16</b><span>18</span><span>19</span><span>20</span><span>21</span><span>22</span><span>23</span><span>24</span>
      <b>17</b><span class="hol">25</span><span>26</span><span>27</span><span>28</span><span>29</span><span>30</span>
    </div></div>
    <div class="month"><h4>May 2021</h4><div class="days">
      <span class="dh">W</span><span class="dh">S</span><span class="dh">M</span><span class="dh">T</span><span class="dh">W</span><span class="dh">T</span><span class="dh">F</span><span class="dh">S</span>
      <b>17</b><span class="from-sat">1</span>
      <b>18</b><span>2</span><span>3</span><span>4</span><span>5</span><span>6</span><span>7</span><span>8</span>
      <b>19</b><span>9</span><span>10</span><span>11</span><span>12</span><span>13</span><span>14</span><span>15</span>
      <b>20</b><span>16</span><span>17</span><span>18</span><span>19</span><span>20</span><span>21</span><span>22</span>
      <b>21</b><span>23</span><span>24</span><span>25</span><span>26</span><span>27</span><span>28</span><span>29</span>
      <b>22</b><span>30</span><span class="hol">31</span>
    </div></div>
    <div class="month"><h4>June 2021</h4><div class="days">
      <span class="dh">W</span><span class="dh">S</span><span class="dh">M</span><span class="dh">T</span><span class="dh">W</span><span class="dh">T</span><span class="dh">F</span><span class="dh">S</span>
      <b>22</b><span class="from-tue">1</span><span>2</span><span>3</span><span>4</span><span>5</span>
      <b>23</b><span>6</span><span>7</span><span>8</span><span>9</span><span>10</span><span>11</span><span>12</span>
      <b>24</b><span>13</span><span class="hol">14</span><span>15</span><span>16</span><span>17</span><span>18</span><span>19</span>
      <b>25</b><span>20</span><span>21</span><span>22</span><span>23</span><span>24</span><span>25</span><span>26</span>
      <b>26</b><span>27</span><span>28</span><span>29</span><span>30</span>
    </div></div>
    <div class="month"><h4>July 2021</h4><div class="days">
      <span class="dh">W</span><span class="dh">S</span><span class="dh">M</span><span class="dh">T</span><span class="dh">W</span><span class="dh">T</span><span class="dh">F</span><span class="dh">S</span>
      <b>26</b><span class="from-thu">1</span><span>2</span><span>3</span>
      <b>27</b><span>4</span><span>5</span><span>6</span><span>7</span><span>8</span><span>9</span><span>10</span>
      <b>28</b><span>11</span><span>12</span><span>13</span><span>14</span><span>15</span><span>16</span><span>17</span>
      <b>29</b><span>18</span><span>19</span><span>20</span><span>21</span><span>22</span><span>23</span><span>24</span>
      <b>30</b><span>25</span><span>26</span><span>27</span><span>28</span><span>29</span><span>30</span><span>31</span>
    </div></div>
    <div class="month"><h4>August 2021</h4><div class="days">
      <span class="dh">W</span><span class="dh">S</span><span class="dh">M</span><span class="dh">T</span><span class="dh">W</span><span class="dh">T</span><span class="dh">F</span><span class="dh">S</span>
      <b>31</b><span class="from-sun">1</span><span>2</span><span>3</span><span>4</span><span>5</span><span>6</span><span>7</span>
      <b>32</b><span>8</span><span>9</span><span>10</span><span>11</span><span>12</span><span>13</span><span>14</span>
      <b>33</b><span>15</span><span>16</span><span>17</span><span>18</span><span>19</span><span>20</span><span>21</span>
      <b>34</b><span>22</span><span>23</span><span>24</span><span>25</span><span>26</span><span>27</span><span>28</span>
      <b>35</b><span>29</span><span>30</span><span>31</span>
    </div></div>
    <div class="month"><h4>September 2021</h4><div class="days">
      <span class="dh">W</span><span class="dh">S</span><span class="dh">M</span><span class="dh">T</span><span class="dh">W</span><span class="dh">T</span><span class="dh">F</span><span class="dh">S</span>
      <b>35</b><span class="from-wed">1</span><span>2</span><span>3</span><span>4</span>
      <b>36</b><span>5</span><span>6</span><span>7</span><span>8</span><span>9</span><span>10</span><span>11</span>
      <b>37</b><span>12</span><span>13</span><span>14</span><span>15</span><span>16</span><span>17</span><span>18</span>
      <b>38</b><span>19</span><span>20</span><span>21</span><span>22</span><span>23</span><span>24</span><span>25</span>
      <b>39</b><span>26</span><span>27</span><span>28</span><span>29</span><span>30</span>
    </div></div>
    <div class="month"><h4>October 2021</h4><div class="days">
      <span class="dh">W</span><span class="dh">S</span><span class="dh">M</span><span class="dh">T</span><span class="dh">W</span><span class="dh">T</span><span class="dh">F</span><span class="dh">S</span>
      <b>39</b><span class="from-fri">1</span><span>2</span>
      <b>40</b><span>3</span><span class="hol">4</span><span>5</span><span>6</span><span>7</span><span>8</span><span>9</span>
      <b>41</b><span>10</span><span>11</span><span>12</span><span>13</span><span>14</span><span>15</span><span>16</span>
      <b>42</b><span>17</span><span>18</span><span>19</span><span>20</span><span>21</span><span>22</span><span>23</span>
      <b>43</b><span>24</span><span>25</span><span>26</span><span>27</span><span>28</span><span>29</span><span>30</span>
      <b>44</b><span>31</span>
    </div></div>
    <div class="month"><h4>November 2021</h4><div class="days">
      <span class="dh">W</span><span class="dh">S</span><span class="dh">M</span><span class="dh">T</span><span class="dh">W</span><span class="dh">T</span><span class="dh">F</span><span class="dh">S</span>
      <b>44</b><span class="from-mon">1</span><span>2</span><span>3</span><span>4</span><span>5</span><span>6</span>
      <b>45</b><span>7</span><span>8</span><span>9</span><span>10</span><span>11</span><span>12</span><span>13</span>
      <b>46</b><span>14</span><span>15</span><span>16</span><span>17</span><span>18</span><span>19</span><span>20</span>
      <b>47</b><span>21</span><span>22</span><span>23</span><span>24</span><span>25</span><span>26</span><span>27</span>
      <b>48</b><span>28</span><span>29</span><span>30</span>
    </div></div>
    <div class="month"><h4>December 2021</h4><div class="days">
      <span class="dh">W</span><span class="dh">S</span><span class="dh">M</span><span class="dh">T</span><span class="dh">W</span><span class="dh">T</span><span class="dh">F</span><span class="dh">S</span>
      <b>48</b><span class="from-wed">1</span><span>2</span><span>3</span><span>4</span>
      <b>49</b><span>5</span><span>6</span><span>7</span><span>8</span><span>9</span><span>10</span><span>11</span>
      <b>50</b><span>12</span><span>13</span><span>14</span><span>15</span><span>16</span><span>17</span><span>18</span>
      <b>51</b><span>19</span><span>20</span><span>21</span><span>22</span><span>23</span><span>24</span><span class="hol">25</span>
      <b>52</b><span class="hol">26</span><span>27</span><span>28</span><span>29</span><span>30</span><span>31</span>
    </div></div>
  </div>
</section>

</body>
</html>
```